Business Card Design

Quindraw

Industry/Entity Type

Business

Contact Information for Business Card

Harbour Crest Lotto
Harbour Crest Shopping Centre
Kiosk 1 No.47 Marlow Brook way
Marlow Heights
Dale Hoskins
0413528846

```html
<!DOCTYPE html>
<html lang="en">
<head>
<meta charset="utf-8">
<title>Harbour Crest Lotto – Business Card</title>
<link rel="stylesheet" href="https://fonts.googleapis.com/css2?family=Open+Sans:wght@400;600;700&display=swap">
<style>
  :root {
    --stage: #262626;
    --purple: #662483;
    --white: #ffffff;
    --ink: #3c3c3c;
    --grey: #5a5a5a;
    --rule: #6b6b6b;
    --icon: #555555;
    --quin-blue: #1f3f8f;
  }
  * { box-sizing: border-box; margin: 0; padding: 0; }
  html, body {
    width: 1200px; height: 900px; overflow: hidden;
    background: var(--stage);
    font-family: "Open Sans", Arial, sans-serif;
  }
  .canvas { position: relative; width: 1200px; height: 900px; }

  .card {
    position: absolute; width: 640px; height: 366px;
    box-shadow: 0 12px 30px rgba(0,0,0,.45);
    overflow: hidden;
  }

  .brand { font-weight: 700; text-transform: uppercase; line-height: 1.05; }
  .brand__line { display: block; }

  /* Back */
  .card--back { left: 70px; top: 60px; background: var(--purple); }
  .card--back .brand {
    position: absolute; left: 0; right: 0; top: 145px; text-align: center;
    color: var(--white);
  }
  .card--back .brand__line--main { font-size: 46px; letter-spacing: 3px; }
  .card--back .brand__line--sub { font-size: 21px; letter-spacing: 6px; }

  /* Front */
  .card--front { left: 490px; top: 474px; background: var(--white); }
  .card--front .brand {
    position: absolute; right: 34px; top: 34px; text-align: right;
  }
  .card--front .brand__line--main { font-size: 38px; letter-spacing: 3px; color: var(--purple); }
  .card--front .brand__line--sub { font-size: 19px; letter-spacing: 6px; color: var(--grey); }

  .holder {
    position: absolute; left: 40px; right: 0; top: 122px;
    display: flex; align-items: center;
  }
  .holder__name { font-size: 27px; color: var(--ink); white-space: nowrap; }
  .holder__first { color: var(--purple); }
  .holder__rule { flex: 1; height: 2px; background: var(--rule); margin-left: 16px; }

  .contacts {
    position: absolute; left: 40px; top: 174px; list-style: none;
    font-size: 15px; color: var(--ink); line-height: 1.27;
  }
  .contacts li { display: flex; align-items: flex-start; margin-bottom: 6px; }
  .contacts svg { width: 15px; height: 15px; margin: 2px 12px 0 0; fill: var(--icon); flex: none; }
  .contacts .icon--pin { margin-top: 20px; }

  .partner {
    position: absolute; right: 34px; top: 222px;
    display: flex; align-items: center; gap: 8px;
  }
  .partner__name { font-size: 26px; font-weight: 700; color: var(--quin-blue); }
  .partner__dot { width: 18px; height: 18px; border-radius: 50%; background: var(--quin-blue); }

  .band {
    position: absolute; left: 0; right: 0; bottom: 0; height: 48px;
    background: var(--purple);
  }
</style>
</head>
<body>
<main class="canvas">
  <section class="card card--back" aria-label="Card back">
    <p class="brand">
      <span class="brand__line brand__line--main">Harbour Crest</span>
      <span class="brand__line brand__line--sub">Lotto</span>
    </p>
  </section>

  <section class="card card--front" aria-label="Card front">
    <p class="brand">
      <span class="brand__line brand__line--main">Harbour Crest</span>
      <span class="brand__line brand__line--sub">Lotto</span>
    </p>

    <div class="holder">
      <span class="holder__name"><span class="holder__first">Dale</span> Hoskins</span>
      <span class="holder__rule"></span>
    </div>

    <ul class="contacts">
      <li>
        <svg viewBox="0 0 24 24" aria-hidden="true"><path d="M6.6 10.8a15.1 15.1 0 0 0 6.6 6.6l2.2-2.2c.3-.3.7-.4 1-.2 1.1.4 2.3.6 3.6.6.6 0 1 .4 1 1V20c0 .6-.4 1-1 1A17 17 0 0 1 3 4c0-.6.4-1 1-1h3.5c.6 0 1 .4 1 1 0 1.3.2 2.5.6 3.6.1.3 0 .7-.2 1z"/></svg>
        <span>0413528846</span>
      </li>
      <li>
        <svg class="icon--pin" viewBox="0 0 24 24" aria-hidden="true"><path d="M12 2a7 7 0 0 0-7 7c0 5.2 7 13 7 13s7-7.8 7-13a7 7 0 0 0-7-7zm0 9.5A2.5 2.5 0 1 1 12 6.5a2.5 2.5 0 0 1 0 5z"/></svg>
        <span>Harbour Crest Shopping Centre<br>Kiosk 1 No.47 Marlow Brook way<br>Marlow Heights</span>
      </li>
      <li>
        <svg viewBox="0 0 24 24" aria-hidden="true"><path d="M2 5h20v14H2zm2 2v.5l8 5 8-5V7zm0 2.8V17h16V9.8l-8 5z"/></svg>
        <span>dalehoskins@harbournet.com</span>
      </li>
    </ul>

    <div class="partner">
      <span class="partner__name">Quindraw</span>
      <span class="partner__dot"></span>
    </div>

    <div class="band"></div>
  </section>
</main>
</body>
</html>
```